Präsentationsvorlagen für Start-up im Bereich Unternehmensberatung
Zielgruppe
Start-up im Bereich Unternehmensberatung. Zielgruppen sind CEO und HR Verantwortliche in Großunternehmen. Suchen klares, hochwertiges Design eher an Frauen als an Männer gerichtet. Haben bereits Vorlagen erarbeitet, diese sind aber zu technisch orientiert. Erwartet wird eine neue pptx Präsentation
Aufgabenstellung
Bilder / Texte gemäss Website respektive bestehender PPT.

```html
<!DOCTYPE html>
<html lang="de">
<head>
<meta charset="utf-8">
<title>Vivanta – Präsentation</title>
<link rel="stylesheet" href="https://fonts.googleapis.com/css2?family=Roboto+Condensed:wght@400;700&family=Roboto:wght@400;500&display=swap">
<style>
  :root {
    --red: #c3070f;
    --grey: #666666;
    --light: #e4e4e4;
    --bg: #ffffff;
    --white: #ffffff;
  }
  * { margin: 0; padding: 0; box-sizing: border-box; }
  html, body { width: 1200px; height: 3943px; overflow: hidden; background: var(--bg); }
  body { position: relative; font-family: "Roboto", Arial, sans-serif; color: var(--grey); }

  .slide {
    position: absolute; left: 50px; width: 1099px; height: 620px;
    background: var(--white); overflow: hidden;
    box-shadow: 0 2px 10px rgba(0,0,0,.22);
  }
  .wordmark {
    position: absolute; font-family: "Roboto Condensed", sans-serif; font-weight: 700;
    color: var(--red); letter-spacing: 1px; line-height: 1;
  }
  .photo { position: absolute; }
  .heading {
    position: absolute; font-family: "Roboto Condensed", sans-serif; font-weight: 400;
    color: var(--red); line-height: 1.2; text-transform: uppercase;
  }
  .footer-line { position: absolute; left: 109px; top: 590px; width: 938px; height: 1px; background: var(--red); opacity: .6; }
  .page-no { position: absolute; left: 1058px; top: 582px; font-size: 13px; font-weight: 500; color: var(--red); }
  .copy { position: absolute; font-size: 16px; line-height: 1.3; color: var(--grey); }

  .s-cover { top: 58px; left: 46px; }
  .s-cover .photo { inset: 0; background: radial-gradient(ellipse at 45% 40%, #cfd8e4 0%, #aebfd6 45%, #8ea7c8 100%); }

  .s-toc { top: 713px; }
  .s-toc .photo { left: 633px; top: 0; width: 466px; height: 620px; background: linear-gradient(160deg, #a99a83 0%, #6e655b 45%, #3d4250 100%); }
  .toc-list { position: absolute; left: 0; top: 0; list-style: none; }
  .toc-item { position: absolute; left: 0; width: 600px; height: 50px; display: flex; align-items: baseline; }
  .toc-num { width: 175px; text-align: right; font-family: "Roboto Condensed", sans-serif; font-size: 40px; color: var(--red); }
  .toc-label { margin-left: 14px; font-size: 20px; color: var(--grey); text-transform: uppercase; }

  .s-about { top: 1358px; }
  .s-about .photo { left: 0; top: 251px; width: 1099px; height: 369px; background: linear-gradient(90deg, #d9dde0 0%, #bfc3c2 40%, #9aa09c 70%, #c6ccd0 100%); }
  .about-box {
    position: absolute; left: 602px; top: 94px; width: 397px; height: 454px;
    background: var(--red); color: var(--white); padding: 32px 30px; font-size: 14.5px; line-height: 1.33;
  }
  .about-box p + p { margin-top: 18px; }

  .s-concept { top: 2001px; }
  .flower { position: absolute; left: 392px; top: 173px; width: 341px; height: 337px; overflow: visible; }
  .ring-label { font-family: "Roboto Condensed", sans-serif; font-size: 15px; font-weight: 700; fill: #fff; }

  .s-process { top: 2652px; }
  .step-text { position: absolute; text-align: center; font-size: 16px; line-height: 1.25; color: #444; }

  .s-end { top: 3301px; }
  .s-end .photo { top: 0; height: 620px; background: radial-gradient(circle at 50% 50%, #8d8d8d 0%, #5a5a5a 60%, #3c3c3c 100%); }
  .tagline { position: absolute; left: 0; width: 100%; text-align: center; font-family: "Roboto Condensed", sans-serif; font-size: 56px; color: #6a6a6a; }
  .tagline span { color: var(--red); }
</style>
</head>
<body>

<section class="slide s-cover">
  <div class="photo" role="img" aria-label="Unscharfes Foto einer Person im hellblauen Hemd hinter einer Glasscheibe mit handgeschriebenem Wort"></div>
  <div class="wordmark" style="left:790px; top:40px; font-size:74px;">VIVANTA</div>
</section>

<section class="slide s-toc">
  <h1 class="heading" style="left:126px; top:52px; font-size:58px;">Inhalt</h1>
  <ul class="toc-list">
    <li class="toc-item" style="top:182px;"><span class="toc-num">3</span><span class="toc-label">Wer wir sind</span></li>
    <li class="toc-item" style="top:253px;"><span class="toc-num">6</span><span class="toc-label">Ihre Herausforderungen</span></li>
    <li class="toc-item" style="top:323px;"><span class="toc-num">10</span><span class="toc-label">Unser Konzept</span></li>
    <li class="toc-item" style="top:394px;"><span class="toc-num">12</span><span class="toc-label">Erfolgsfaktoren</span></li>
    <li class="toc-item" style="top:464px;"><span class="toc-num">14</span><span class="toc-label">Resultate</span></li>
  </ul>
  <div class="wordmark" style="left:28px; top:574px; font-size:28px;">VIVANTA</div>
  <div class="photo" role="img" aria-label="Foto: Teamhände übereinander gelegt in der Mitte eines Kreises"></div>
</section>

<section class="slide s-about">
  <h2 class="heading" style="left:52px; top:46px; font-size:58px; line-height:74px;">Wer wir sind und<br>was wir bewegen</h2>
  <div class="photo" role="img" aria-label="Foto: Mitarbeitende an Computern in einem hellen Büro"></div>
  <div class="about-box">
    <p>Wir sind ein StartUp mit über 100 Jahre Erfahrung</p>
    <p>Spezialisten aus den Bereichen Sport, Ernährung, Gesundheit, Motivation, Rhetorik &amp; Führung sowie IT haben ein einzigartiges, in sich geschlossenes System entwickelt</p>
    <p>Durch die Zusammenarbeit mit Vivanta machen Sie Veränderungen erlebbar. Unser Konzept startet bei der Information und endet bei der erfolgreichen Umsetzung.</p>
    <p>Die Menschen die wir erreichen, liegen eigentlich recht bequem im Leben. Alles läuft mehr oder weniger in geordneten Bahnen. Und trotzdem fehlt es an Antrieb und Zufriedenheit, die Leistungskurve hat in den letzten Jahren merklich ab- und der BMI zugenommen.</p>
  </div>
</section>

<section class="slide s-concept">
  <h2 class="heading" style="left:52px; top:50px; font-size:46px;">Unser Konzept</h2>
  <p class="copy" style="left:120px; top:199px; width:262px; text-align:right;">Tipps &amp; Tricks für einen energie-geladenen Tag! Oder was passiert, wenn Sie nichts tun.</p>
  <p class="copy" style="left:136px; top:403px; width:252px; text-align:right;">In regelmässigen Workshops besprechen wir den Status Quo und passen gegebenenfalls die Massnahmen an.</p>
  <p class="copy" style="left:753px; top:156px; width:310px;">Was ist deine Vorstellung von dir selbst? Welche Dinge beeinflussen deinen Tag, was bewegt dich?<br>Auf Basis der einzelnen Workshopresultate werden spezifische, von Profis besprochene Autosuggestions-Aufnahmen erstellt</p>
  <p class="copy" style="left:753px; top:422px; width:310px;">Hier startet der eingentliche Arbeitsprozess. In einer App werden die Resultate aus dem Workshop abgebildet, die spezifischen Pläne hinterlegt und die Regel-kommunikation aufgenommen</p>

  <svg class="flower" viewBox="0 0 341 337">
    <defs>
      <path id="arc-tl" d="M 20.2 108.9 A 70 70 0 0 1 121 24.4"/>
      <path id="arc-tr" d="M 231 19.2 A 70 70 0 0 1 320.8 108.9"/>
      <path id="arc-bl" d="M 20.2 228.1 A 70 70 0 0 0 109.9 317.8"/>
      <path id="arc-br" d="M 231.1 317.8 A 70 70 0 0 0 320.8 228.1"/>
    </defs>
    <g fill="none" stroke="var(--red)" stroke-width="30">
      <circle cx="86" cy="85" r="70"/>
      <circle cx="255" cy="85" r="70"/>
      <circle cx="86" cy="252" r="70"/>
      <circle cx="255" cy="252" r="70"/>
    </g>
    <g class="ring-label" text-anchor="middle">
      <text dy="5"><textPath href="#arc-tl" startOffset="50%">Kick-Off Vortrag</textPath></text>
      <text dy="5"><textPath href="#arc-tr" startOffset="50%">Workshop</textPath></text>
      <text dy="5"><textPath href="#arc-bl" startOffset="50%">Status Workshop</textPath></text>
      <text dy="5"><textPath href="#arc-br" startOffset="50%">Umsetzung</textPath></text>
    </g>
    <circle cx="170" cy="168" r="68" fill="#fff" stroke="var(--light)" stroke-width="3"/>
    <rect x="113" y="160" width="10" height="10" fill="var(--red)"/>
    <text x="178" y="170" text-anchor="middle" font-family="Roboto Condensed, sans-serif" font-size="15" font-weight="700" fill="#222">NORDTAL OPTIK</text>
  </svg>

  <div class="wordmark" style="left:31px; top:579px; font-size:26px;">VIVANTA</div>
  <div class="footer-line"></div>
  <div class="page-no">10</div>
</section>

<section class="slide s-process">
  <h2 class="heading" style="left:61px; top:34px; font-size:46px;">Schlüsselfaktoren | Der Prozess</h2>

  <svg style="position:absolute; left:0; top:0;" width="1099" height="620" viewBox="0 0 1099 620">
    <g fill="none" stroke="var(--red)" stroke-width="44">
      <path d="M 104 300 A 118 118 0 0 1 338 280"/>
      <path d="M 453 390 A 93 93 0 0 0 640 373"/>
      <path d="M 754 300 A 118 118 0 0 1 988 280"/>
    </g>
    <g fill="var(--red)">
      <polygon points="292,272 384,272 345,338"/>
      <polygon points="590,382 690,364 634,320"/>
      <polygon points="942,272 1034,272 995,338"/>
    </g>
    <g fill="#d9d9d9" stroke="#fff" stroke-width="4">
      <circle cx="218" cy="325" r="41"/>
      <circle cx="546" cy="390" r="41"/>
      <circle cx="868" cy="325" r="41"/>
    </g>
    <g fill="#fff" font-family="Roboto Condensed, sans-serif" font-size="40" text-anchor="middle">
      <text x="218" y="339">1</text>
      <text x="546" y="404">2</text>
      <text x="868" y="339">3</text>
    </g>
  </svg>

  <p class="step-text" style="left:118px; top:391px; width:200px;">Kick-Off Vortrag u.a. am Beispiel von Arbeitspausen "das habe ich mir jetzt aber verdient"</p>
  <p class="step-text" style="left:430px; top:212px; width:232px;">Der Unterschied zwischen Willenskraft und Vorstellungs-vermögen, oder die Antworten auf die Frage nach dem Warum?</p>
  <p class="step-text" style="left:808px; top:396px; width:120px;">Start des 6-monatigen Prozesses</p>

  <div class="wordmark" style="left:28px; top:579px; font-size:26px;">VIVANTA</div>
  <div class="footer-line"></div>
  <div class="page-no">13</div>
</section>

<section class="slide s-end">
  <div class="photo" style="left:0; width:296px;" role="img" aria-label="Foto: graue Kieselsteine mit einem roten Stein"></div>
  <div class="photo" style="left:915px; width:184px;" role="img" aria-label="Foto: graue Kieselsteine"></div>
  <div class="wordmark" style="left:296px; width:619px; top:185px; text-align:center; font-size:110px;">VIVANTA</div>
  <p class="tagline" style="left:296px; width:619px; top:405px;">stay unique<span>!</span></p>
</section>

</body>
</html>
```